New Business Card Design Project

We require a business card design for Zelvaquin, a newly established Indian company.
Our focus is on the development, manufacturing, and export of a diverse array of pharmaceutical products on a global scale. The card should convey a professional appearance, as our primary markets are in Africa, China, and Southeast Asian nations.
We envision a two-sided business card, with the reverse side dedicated to a logo set against a solid color or an elegantly designed pattern. The corners should be rounded. We would appreciate seeing both horizontal and vertical design options. We trust the designer to utilize their expertise in creating this design.

The content for the business card is included in the attached Word file.

Target Market(s)

Our primary markets are in Africa, China, and Southeast Asian, Latin America, Maldives, Sri Lanka

Industry/Entity Type

Pharmaceutical Manufacturing and Export

Contact Information for Business Card

Colors

Designer to choose colors to be used in the design.

Requirements
Must have
• The reverse side of the business card features solely the logo along with the tagline, "Wellness in Reach."
Should not have
• The logo should not exceed two instances, encompassing both the front and back sides of the card.

```html
<!DOCTYPE html>
<html lang="en">
<head>
<meta charset="utf-8">
<title>Zelvaquin Business Card</title>
<link rel="stylesheet" href="https://fonts.googleapis.com/css2?family=Montserrat:wght@700;800&family=Open+Sans:wght@400;600&family=Poppins:wght@400&display=swap">
<style>
  :root {
    --stage: #232323;
    --card-dark: #1d1e22;
    --brand-blue: #2ea7e0;
    --accent-coral: #f0604c;
    --white: #ffffff;
    --text-light: #e9e9ea;
  }
  * { box-sizing: border-box; margin: 0; padding: 0; }
  html, body {
    width: 1200px; height: 780px; overflow: hidden;
    background: var(--stage);
  }
  .stage { position: relative; width: 1200px; height: 780px; }
  .card {
    position: absolute; width: 540px; height: 310px;
    border-radius: 26px; overflow: hidden;
    box-shadow: 0 18px 40px rgba(0,0,0,0.55);
  }

  /* Reverse side */
  .card-back {
    left: 40px; top: 235px;
    background: var(--brand-blue);
    display: flex; align-items: center; justify-content: center;
  }
  .back-lockup { display: flex; flex-direction: column; align-items: flex-end; }
  .brand-lockup { display: flex; align-items: center; gap: 14px; }
  .brand-dot { width: 22px; height: 22px; border-radius: 50%; background: var(--white); flex: none; }
  .brand-name-back {
    font-family: "Montserrat", sans-serif; font-weight: 800;
    font-size: 62px; line-height: 1.1; color: var(--white); letter-spacing: 0.5px;
  }
  .tagline {
    margin-top: 6px;
    font-family: "Poppins", sans-serif; font-size: 14px;
    color: var(--white); letter-spacing: 0.5px;
  }

  /* Front side */
  .card-front { left: 620px; top: 235px; background: var(--card-dark); }
  .title-bar {
    position: absolute; right: 18px; top: 0; width: 12px; height: 64px;
    background: var(--brand-blue);
  }
  .person { position: absolute; right: 44px; top: 20px; text-align: right; }
  .person-name {
    font-family: "Montserrat", sans-serif; font-size: 24px; font-weight: 700;
    letter-spacing: 1px; line-height: 1.2; white-space: nowrap;
  }
  .person-first { color: var(--brand-blue); }
  .person-last { color: var(--accent-coral); font-family: "Open Sans", sans-serif; font-weight: 400; }
  .person-role {
    font-family: "Open Sans", sans-serif; font-size: 12px; color: var(--white);
    margin-top: 2px; letter-spacing: 0.5px;
  }
  .brand-front {
    position: absolute; left: 36px; top: 104px;
    display: flex; align-items: center; gap: 10px;
  }
  .brand-front .brand-dot { width: 16px; height: 16px; background: var(--accent-coral); }
  .brand-name-front {
    font-family: "Montserrat", sans-serif; font-weight: 800; font-size: 40px;
    line-height: 1.1; color: var(--brand-blue);
  }
  .address {
    position: absolute; left: 40px; top: 170px; font-style: normal;
    font-family: "Open Sans", sans-serif; font-size: 13px; line-height: 1.45;
    color: var(--text-light);
  }
  .contacts {
    position: absolute; left: 40px; top: 220px; list-style: none;
    font-family: "Open Sans", sans-serif; font-size: 13px; color: var(--text-light);
  }
  .contacts li { display: flex; align-items: center; gap: 10px; height: 22px; white-space: nowrap; }
  .contacts svg { width: 14px; height: 14px; flex: none; }
</style>
</head>
<body>
<main class="stage">

  <section class="card card-back" aria-label="Business card reverse side">
    <div class="back-lockup">
      <div class="brand-lockup">
        <span class="brand-dot"></span>
        <span class="brand-name-back">Zelvaquin</span>
      </div>
      <p class="tagline">Wellness in Reach.</p>
    </div>
  </section>

  <section class="card card-front" aria-label="Business card front side">
    <span class="title-bar"></span>
    <div class="person">
      <p class="person-name"><span class="person-first">Ravik</span> <span class="person-last">S. Tendal</span></p>
      <p class="person-role">CEO</p>
    </div>

    <div class="brand-front">
      <span class="brand-dot"></span>
      <span class="brand-name-front">Zelvaquin</span>
    </div>

    <address class="address">
      12, Suman Vihar,<br>
      Nandgaon, 431205, India
    </address>

    <ul class="contacts">
      <li>
        <svg viewBox="0 0 14 14" aria-hidden="true"><rect x="3" y="1" width="8" height="12" rx="1.5" fill="none" stroke="var(--accent-coral)" stroke-width="1.4"/></svg>
        +91 98765 01234
      </li>
      <li>
        <svg viewBox="0 0 14 14" aria-hidden="true"><circle cx="7" cy="7" r="6" fill="none" stroke="var(--brand-blue)" stroke-width="1.3"/><ellipse cx="7" cy="7" rx="2.6" ry="6" fill="none" stroke="var(--brand-blue)" stroke-width="1"/><line x1="1" y1="7" x2="13" y2="7" stroke="var(--brand-blue)" stroke-width="1"/></svg>
        www.zelvaquin.com
      </li>
      <li>
        <svg viewBox="0 0 14 14" aria-hidden="true"><rect x="1" y="3" width="12" height="9" rx="1" fill="none" stroke="var(--accent-coral)" stroke-width="1.3"/><polyline points="1.5,3.5 7,8 12.5,3.5" fill="none" stroke="var(--accent-coral)" stroke-width="1.3"/></svg>
        rtendal@zelvaquin.com
      </li>
    </ul>
  </section>

</main>
</body>
</html>
```